Aviation Maintenance & Aircraft Cleaning Website

We need a fairly simple modern sleek website . Our company does aviation maintenance , aircraft cleaning , maintenance tracking . We work on KT420 HELICOPTERS , BELVANKO T82 HELICOPTERS , MORVELL TARRANT 512 HELICOPTERS. We would like a website that can be mobile as well with future ideas that an app where you could book cleanings and maintenance . Right now the biggest thing is for our customer to see a website , be able to book our services online and see our staff . the website must be modern and clean .

Target Market(s)

Aviation maintenance , aviation cleaning ,

Logo Text

TW but 1 image unlike the one i uploaded which is two . Im open for different aviation designs

Number of Pages Required

5+ page

Font styles to use
Serif

Requirements
Must have
• Home page , Aircraft Maintenance , Aircraft Cleaning , About Us , Contact , Careers

TW Aviation is insured and all of our mechanics are licensed by the NQB with an Airframe & Powerplant rating. ( FRONT PAGE )

Home page should have a simple nice picture of a KT420 or Belvanko T82 . My Logo as you can see seems like two logos . i would like 1 logo and made of the two if possible . (New ideas are welcome . )

Book a Cleaning Calendar should in the aircraft cleaning page . The aircraft cleaning page should have a picture of cleaning a helicopter or private jet .

Aircraft maintenance page should have a mechanic working on a helicopter . The Page should have a fast way to contact us .

We are a mobile AOG team who is available 24/7 . What we do
Scheduled & Unscheduled aircraft maintenance
Major & Minor repairs
STC installations
Aircraft Weight & Balance
Aircraft Painting
Aircraft Cleaning
Maintenance Tracking Utilizing Tracking Programs or spreadsheets
Removal & Installation of Components
Aircraft Pre Buy Inspections
Nice to have
• modern , sleek , aviation

Meet the Staff

Picture with Headset on flying in a helicopter

CEO Mateus Ferreira

Mateus Has been an aircraft mechanic for over 10 years . He has worked for the largest sightseeing & charter tourism company in the New York City area as well as repair stations & manufacturers. He has aircraft specific training to the Kestrane KT420 & Vornel 2K4. He has worked on several airframes including the Belvanko T82 and the Morvell 512. He has held every position in an aircraft maintenance department from mechanic up to Director of Maintenance . His work ethic and ability to manage mechanics in a organized and structured way gives any department or inspection a clear direction .

About Us

TW Aviation Services is company with aircraft maintenance experience . We focus on inspections of aircraft . Our Aircraft Mechanics who are pilots and IA's have experience many aircraft but specialize in the Kestrane KT420 , KT425 , KT435 . The Belvanko T82 and Morvell Tarrant 512 . Our focus is safety and to maintain aircraft day in and day out so our customer can operate the aircraft safely while keeping up with all the manufacturers inspections .

We know aircraft maintenance & maintenance planning . Leave the technical and tedious things to us . Get in your aircraft and fly knowing you have the best maintenance crew in the business.

```html
<!DOCTYPE html>
<html lang="en">
<head>
<meta charset="utf-8">
<title>About Us — TW Aviation</title>
<link rel="stylesheet" href="https://fonts.googleapis.com/css2?family=Lora:ital,wght@0,400;0,500;0,700;1,400&family=Lato:wght@400;700;900&display=swap">
<style>
:root{
  --red:#f04a32;
  --ink:#2b2b2b;
  --muted:#555555;
  --rule:#d9d9d9;
  --white:#ffffff;
  --black:#000000;
  --hero-deep:#1d2a55;
  --hero-warm:#6b5a44;
  --panel:#121417;
}
*{box-sizing:border-box;margin:0;padding:0}
html,body{width:1200px;height:3934px;overflow:hidden}
body{position:relative;background:var(--white);color:var(--ink);font-family:'Lora',Georgia,serif}
.abs{position:absolute}
.label{font-family:'Lato',Arial,sans-serif;font-weight:700;font-size:13px;letter-spacing:1.6px;color:var(--red);text-transform:uppercase}
.label .slashes{font-family:'Lora',serif;font-style:italic;font-weight:400;font-size:19px;letter-spacing:0;margin-right:12px}
.brand{font-family:'Lato',Arial,sans-serif;color:var(--white);display:flex;align-items:baseline;gap:10px}
.brand b{font-weight:900;font-size:19px;letter-spacing:1px}
.brand span{font-weight:700;font-size:9px;letter-spacing:4px}

/* hero */
.hero{left:0;top:0;width:1200px;height:675px;overflow:hidden}
.hero-photo{position:absolute;inset:0;background:
  radial-gradient(ellipse at 72% 40%,rgba(150,140,120,.55),transparent 55%),
  radial-gradient(ellipse at 45% 55%,rgba(120,70,50,.45),transparent 45%),
  linear-gradient(100deg,var(--hero-deep) 0%,#2e3552 40%,var(--hero-warm) 80%,#8d8170 100%)}
.hero-shade{position:absolute;inset:0;background:linear-gradient(90deg,rgba(20,30,70,.55),rgba(20,25,50,.15))}
.hero-rail{position:absolute;left:38px;top:0;width:1px;height:675px;background:rgba(255,255,255,.25)}
.hero .brand{position:absolute;left:73px;top:40px}
.menu{position:absolute;left:1084px;top:40px;width:28px;height:18px}
.hero h1{position:absolute;left:87px;top:190px;font-weight:700;font-size:46px;color:var(--white);letter-spacing:.5px}
.hero p{position:absolute;left:87px;top:290px;width:430px;font-size:15px;line-height:22px;color:rgba(255,255,255,.82)}
.scroll{position:absolute;left:10px;top:552px;font-family:'Lato',sans-serif;font-size:8px;letter-spacing:1.5px;color:rgba(255,255,255,.7);writing-mode:vertical-rl;transform:rotate(180deg)}
.scroll-arrow{position:absolute;left:12px;top:632px}

/* services intro */
.blob{left:90px;top:755px}
.service-title{left:87px;top:800px;font-style:italic;font-size:48px;line-height:62px;color:var(--ink)}
.service-title .line2{display:block;padding-left:218px}
.service-rule{left:87px;top:898px;width:208px;height:3px;background:var(--red)}
.cal{left:139px;top:872px}
.tracking-label{left:664px;top:1111px}
.tracking-text{left:692px;top:1159px;width:425px;font-size:16px;line-height:30px;color:var(--muted)}

/* staff */
.hands{left:101px;top:1490px;font-weight:700;font-size:45px;line-height:63px;letter-spacing:1.5px;text-transform:uppercase;color:var(--ink)}
.staff-label{left:101px;top:1719px}
.staff{left:0;top:1828px;width:1200px;height:673px}
.staff-photo{position:absolute;left:0;top:0;width:508px;height:673px;background:linear-gradient(160deg,#8e9399 0%,#5a5f66 45%,#2c2f34 100%)}
.staff-panel{position:absolute;left:508px;top:0;width:692px;height:673px;background:
  radial-gradient(ellipse at 30% 30%,rgba(70,80,95,.55),transparent 60%),
  linear-gradient(180deg,#1f242b 0%,var(--panel) 60%,#08090a 100%)}
.staff-rule{position:absolute;left:508px;top:75px;width:692px;height:1px;background:rgba(255,255,255,.22)}
.staff-head{position:absolute;left:644px;top:174px;display:flex;align-items:baseline}
.staff-name{font-family:'Lato',sans-serif;font-weight:700;font-size:16px;letter-spacing:1.4px;color:var(--white);margin-right:32px}
.staff-bio{position:absolute;left:644px;top:222px;width:425px;font-size:16px;line-height:30px;color:rgba(255,255,255,.88)}

/* careers */
.grow{left:101px;top:2674px;font-weight:700;font-size:46px;line-height:63px;color:var(--ink)}
.roles-label{left:116px;top:2851px}
.role-list{width:400px;list-style:none}
.role-list li{height:71px;border-bottom:1px solid var(--rule);display:flex;align-items:center;font-size:16px;color:var(--ink)}
.role-list .num{width:29px;height:29px;border-radius:50%;background:#d6d6d6;font-family:'Lato',sans-serif;font-size:11px;display:flex;align-items:center;justify-content:center;margin-right:10px;color:#333}
.roles-left{left:136px;top:2943px}
.roles-right{left:682px;top:2943px}
.btn{display:flex;align-items:center;justify-content:center;gap:8px;background:var(--red);color:var(--white);font-family:'Lato',sans-serif;font-weight:900;font-size:11px;letter-spacing:1.3px;text-transform:uppercase}
.show-more{left:921px;top:3205px;width:163px;height:50px}

/* footer */
.footer{left:0;top:3411px;width:1200px;height:523px;background:var(--black)}
.footer-rule{position:absolute;left:0;top:151px;width:1200px;height:1px;background:rgba(255,255,255,.2)}
.footer .brand{position:absolute;left:89px;top:240px}
.footer-nav a{position:absolute;font-size:15px;color:rgba(255,255,255,.78);text-decoration:none}
.copy{position:absolute;left:692px;top:318px;font-family:'Lato',sans-serif;font-size:9px;letter-spacing:.5px;color:rgba(255,255,255,.75)}
.social{position:absolute;top:320px;width:7px;height:7px;border-radius:50%;background:rgba(255,255,255,.85)}
.contact{position:absolute;left:692px;top:381px;width:162px;height:48px}
</style>
</head>
<body>

<header class="abs hero">
  <div class="hero-photo" role="img" aria-label="Close-up of a helicopter turbine engine under maintenance"></div>
  <div class="hero-shade"></div>
  <div class="hero-rail"></div>
  <div class="brand"><b>TW</b><span>AVIATION</span></div>
  <svg class="menu" viewBox="0 0 28 18" aria-label="Menu"><path d="M0 1h28M0 9h28M0 17h28" stroke="#fff" stroke-width="1.6"/></svg>
  <h1>About Us</h1>
  <p>TW Aviation Services is a company with aircraft maintenance experience with focus on safety inspections and maintenance planning. For over 10 years our clients have entrusted us the safety of their aircraft.</p>
  <div class="scroll">SCROLL DOWN</div>
  <svg class="scroll-arrow abs" width="10" height="14" viewBox="0 0 10 14"><path d="M5 0v12M1 8l4 4 4-4" fill="none" stroke="#fff" stroke-width="1"/></svg>
</header>

<section>
  <svg class="abs blob" width="345" height="325" viewBox="0 0 345 325"><path d="M180 5c70-10 140 30 160 80 15 45-40 70-60 100-25 40 20 110-40 135-70 25-190-10-225-80C-10 170 20 70 90 35 120 18 150 9 180 5z" fill="#f3f3f3"/></svg>
  <h2 class="abs service-title">Scheduled and<span class="line2">Unscheduled</span>aircraft maintenance</h2>
  <div class="abs service-rule"></div>
  <svg class="abs cal" width="18" height="18" viewBox="0 0 18 18"><rect x="1" y="3" width="16" height="14" rx="1.5" fill="var(--red)"/><rect x="4" y="0" width="2" height="5" fill="var(--red)"/><rect x="12" y="0" width="2" height="5" fill="var(--red)"/><g fill="#fff"><rect x="4" y="8" width="2.5" height="2"/><rect x="8" y="8" width="2.5" height="2"/><rect x="12" y="8" width="2.5" height="2"/><rect x="4" y="12" width="2.5" height="2"/><rect x="8" y="12" width="2.5" height="2"/><rect x="12" y="12" width="2.5" height="2"/></g></svg>
  <div class="abs label tracking-label"><span class="slashes">//</span>Maintenance Tracking</div>
  <p class="abs tracking-text">Lorem ipsum dolor sit amet, consetetur sadipscing elitr, sed diam nonumy eirmod tempor invidunt ut labore et dolore magna aliquyam erat, sed diam voluptua. At vero eos et accusam et justo duo dolores et ea rebum. Stet clita kasd gubergren, no sea takimata sanctus est Lorem ipsum dolor sit amet. Lorem ipsum</p>
</section>

<section>
  <h2 class="abs hands">Your Aircraft<br>is in good hands</h2>
  <div class="abs label staff-label"><span class="slashes">//</span>Meet the Staff</div>
  <div class="abs staff">
    <div class="staff-photo" role="img" aria-label="The CEO wearing a headset, seated in a helicopter cockpit"></div>
    <div class="staff-panel" role="img" aria-label="Dim view of a city seen from a helicopter cabin"></div>
    <div class="staff-rule"></div>
    <div class="staff-head"><span class="staff-name">Mateus Ferreira</span><span class="label"><span class="slashes">//</span>CEO</span></div>
    <p class="staff-bio">Mateus Has been an aircraft mechanic for over 10 years . He has worked for the largest sightseeing &amp; charter tourism company in the New York City area as well as repair stations &amp; manufacturers. He has aircraft specific training to the Kestrane KT420 &amp; Vornel 2K4. He has worked on several airframes including the Belvanko T82 and the Morvell 512. He has held every position in an aircraft maintenance department from mechanic up to Director of Maintenance . His work ethic and ability to manage mechanics in a organized and structured way gives any department or inspection a clear direction .</p>
  </div>
</section>

<section>
  <h2 class="abs grow">Come grow<br>with us</h2>
  <div class="abs label roles-label"><span class="slashes">//</span>Our Open Roles</div>
  <ul class="abs role-list roles-left">
    <li><span class="num">05</span>Position 01</li>
    <li><span class="num">06</span>Position 01</li>
    <li><span class="num">02</span>Position 01</li>
  </ul>
  <ul class="abs role-list roles-right">
    <li><span class="num">02</span>Position 01</li>
    <li><span class="num">03</span>Position 01</li>
    <li><span class="num">07</span>Position 01</li>
  </ul>
  <a class="abs btn show-more">Show More <svg width="12" height="8" viewBox="0 0 12 8"><path d="M0 4h10M7 1l3 3-3 3" fill="none" stroke="#fff" stroke-width="1.3"/></svg></a>
</section>

<footer class="abs footer">
  <div class="footer-rule"></div>
  <div class="brand"><b>TW</b><span>AVIATION</span></div>
  <nav class="footer-nav">
    <a style="left:692px;top:236px">Aircraft Maintenance</a>
    <a style="left:864px;top:236px">About Us</a>
    <a style="left:950px;top:236px">Careers</a>
    <a style="left:692px;top:267px">Aircraft Cleaning</a>
    <a style="left:864px;top:267px">Contact</a>
  </nav>
  <div class="copy">© 2020 | TW AVIATION</div>
  <span class="social" style="left:867px"></span>
  <span class="social" style="left:905px"></span>
  <span class="social" style="left:944px"></span>
  <a class="btn contact">Contact <svg width="14" height="8" viewBox="0 0 14 8"><path d="M0 4h12M9 1l3 3-3 3" fill="none" stroke="#fff" stroke-width="1.3"/></svg></a>
</footer>

</body>
</html>
```